Tarwin Project Consulting

I need a logo and business card design for a small business operating in the management consulting and contractor space, predominantly in local and state government. I specialise in project management, financial consulting, people and culture, procurement, ICT transformation and contracting for corporate support areas of organisations.

Industry/Entity Type

Business

```html
<!DOCTYPE html>
<html lang="en">
<head>
<meta charset="utf-8">
<title>Tarwin Project Consulting – Business Card</title>
<link href="https://fonts.googleapis.com/css2?family=Quicksand:wght@300;400&display=swap" rel="stylesheet">
<style>
  :root {
    --page-bg: #e4e3e1;
    --card-bg: #f4f4f2;
    --pattern-tone: #e6e6e5;
    --ink: #2b2b2b;
    --ink-soft: #555555;
    --accent-grey: #8a8a8a;
  }
  * { box-sizing: border-box; margin: 0; padding: 0; }
  html, body {
    width: 1200px;
    height: 873px;
    overflow: hidden;
    background: var(--page-bg);
    font-family: "Quicksand", sans-serif;
    color: var(--ink);
  }
  .sheet {
    width: 1200px;
    height: 873px;
    display: flex;
    align-items: center;
    justify-content: center;
    gap: 60px;
  }
  .card {
    position: relative;
    width: 500px;
    height: 286px;
    background: var(--card-bg);
    box-shadow: 0 2px 10px rgba(0,0,0,0.12);
    overflow: hidden;
  }
  /* Contact side */
  .card-contact .person {
    position: absolute;
    top: 52px;
    left: 48px;
    font-size: 30px;
    font-weight: 300;
    letter-spacing: 0.5px;
  }
  .card-contact .person .role {
    font-size: 20px;
    font-weight: 400;
    margin-left: 6px;
  }
  .card-contact .email {
    position: absolute;
    top: 138px;
    left: 48px;
    font-size: 14px;
    font-weight: 400;
  }
  .card-contact .address {
    position: absolute;
    bottom: 44px;
    left: 48px;
    font-size: 15px;
    font-weight: 400;
    color: var(--ink-soft);
  }
  .card-contact .address .postcode { color: var(--accent-grey); }
  /* Brand side */
  .card-brand .pattern {
    position: absolute;
    inset: 0;
    background: linear-gradient(135deg, var(--card-bg) 0%, var(--pattern-tone) 50%, var(--card-bg) 100%);
  }
  .card-brand .brand-name {
    position: absolute;
    top: 112px;
    left: 0;
    right: 0;
    text-align: center;
    font-size: 26px;
    font-weight: 400;
    letter-spacing: 1px;
    color: var(--ink);
  }
  .card-brand .phone {
    position: absolute;
    bottom: 22px;
    right: 26px;
    font-size: 12px;
    font-weight: 400;
    letter-spacing: 3px;
    color: var(--ink-soft);
  }
</style>
</head>
<body>
  <main class="sheet">
    <section class="card card-contact">
      <p class="person">Ellis Warne <span class="role">– Director</span></p>
      <p class="email">ellis@tarwinpc.com</p>
      <p class="address">Larkin Parade Westmere NSW <span class="postcode">2071</span></p>
    </section>
    <section class="card card-brand">
      <div class="pattern" role="img" aria-label="Faint striped hexagon background pattern"></div>
      <p class="brand-name">Tarwin Project Consulting</p>
      <p class="phone">+13 200 614 5582</p>
    </section>
  </main>
</body>
</html>
```